Food company needs package designed to hold recipe cards.

We are a food manufacturer in Texas and we need a design for a small package that will hold 50 recipe cards. The end-product will be sold at retail stores across the USA. The package will be made from 24 pt cardstock. When package box is constructed and glued together, the measurements will be 5.25” x 0.9” x 4.25”.
We would like to see an eye-catching ARTISTIC design. The design does not necessarily need to include images of food to convey the message that recipes are included inside the box. However, if images of food are not included, text / copy will be needed to give details of the contents.
Target Market(s)
Cooks, Foodies, Chefs, Shoppers.
Industry/Entity Type
Food Manufacturer.
Requirements
Must have
- One or more of our logos. Contents included in the box; "Recipe Cards".
Should not have
- Bee graphics, honey dipper graphics. This project is about food, not bees or honey.

```html
<!DOCTYPE html>
<html lang="en">
<head>
<meta charset="utf-8">
<title>Recipe Cards – Box Dieline</title>
<link href="https://fonts.googleapis.com/css2?family=Montserrat:wght@600&display=swap" rel="stylesheet">
<style>
  :root {
    --navy: #020030;
    --orange: #fb9c00;
    --panel-grey: #e6e6e6;
    --lime: #d9dd2a;
    --green: #7fe000;
    --mint: #14e6a0;
    --pumpkin: #e49a10;
    --ornament: rgba(2, 0, 48, 0.16);
    --crease: rgba(255, 255, 255, 0.55);
  }
  * { box-sizing: border-box; margin: 0; padding: 0; }
  html, body { width: 1200px; height: 1200px; overflow: hidden; background: #fff; }
  .dieline { position: relative; width: 1200px; height: 1200px; }
  .flap-svg { position: absolute; left: 0; top: 0; }

  .panel {
    position: absolute;
    background:
      radial-gradient(circle at 5% 20%, var(--lime) 0 18%, transparent 19%),
      radial-gradient(circle at 98% 22%, var(--green) 0 20%, transparent 21%),
      radial-gradient(circle at 8% 92%, var(--pumpkin) 0 22%, transparent 23%),
      radial-gradient(circle at 92% 90%, var(--mint) 0 24%, transparent 25%),
      var(--panel-grey);
  }
  .card { position: absolute; background: rgba(236, 236, 236, 0.93); }
  .frame { position: absolute; border: 1.3px solid var(--navy); }
  .ornament { position: absolute; width: 80px; height: 80px; background: var(--ornament); }
  .ornament.center { width: 72px; height: 28px; }
  .ornament.center-wide { width: 122px; height: 40px; }

  .product-name {
    font-family: "Montserrat", sans-serif;
    font-weight: 600;
    color: var(--navy);
  }
  .spine-label {
    position: absolute;
    font-size: 22px;
    line-height: 1;
    white-space: nowrap;
    letter-spacing: 1px;
  }
  .spine-left { left: 90px; top: 615px; transform: translate(-50%, -50%) rotate(-90deg); }
  .spine-mid { left: 610px; top: 607px; transform: translate(-50%, -50%) rotate(90deg); }

  .back-copy {
    position: absolute;
    left: 206px; top: 548px; width: 272px;
    font-family: "Montserrat", sans-serif;
    font-weight: 600;
    font-size: 11.4px;
    line-height: 15.1px;
    text-transform: uppercase;
    text-align: center;
    color: var(--navy);
  }

  .title-block {
    position: absolute;
    left: 711px; top: 540px; width: 330px;
    text-align: center;
  }
  .title-rule { width: 172px; height: 1.3px; margin: 0 auto 10px; background: var(--navy); }
  .title-text { font-size: 58px; line-height: 1.02; }
  .tagline {
    position: absolute;
    left: 711px; top: 681px; width: 330px;
    text-align: center;
    font-family: "Montserrat", sans-serif;
    font-weight: 600;
    font-size: 9px;
    letter-spacing: 0.2px;
    color: var(--navy);
  }
</style>
</head>
<body>
<div class="dieline">

  <svg class="flap-svg" width="1200" height="1200" viewBox="0 0 1200 1200" aria-hidden="true">
    <polygon points="47,258 102,258 134,324 134,349 47,349" fill="var(--orange)"/>
    <rect x="47" y="349" width="87" height="532" fill="var(--orange)"/>
    <polygon points="47,881 134,881 134,907 102,973 47,973" fill="var(--orange)"/>
    <line x1="47" y1="349" x2="134" y2="349" stroke="var(--crease)" stroke-width="1"/>
    <line x1="47" y1="881" x2="134" y2="881" stroke="var(--crease)" stroke-width="1"/>

    <polygon points="356,881 437,881 437,903" fill="var(--navy)"/>
    <polygon points="437,881 469,881 437,903" fill="var(--orange)"/>

    <polygon points="600,258 654,258 654,349 566,349 566,324" fill="var(--orange)"/>
    <rect x="566" y="349" width="88" height="532" fill="var(--orange)"/>
    <polygon points="566,881 654,881 654,973 600,973 566,907" fill="var(--orange)"/>
    <line x1="566" y1="349" x2="654" y2="349" stroke="var(--crease)" stroke-width="1"/>
    <line x1="566" y1="881" x2="654" y2="881" stroke="var(--crease)" stroke-width="1"/>

    <path d="M654,349 V224 a27,27 0 0 1 27,-27 H1059 a27,27 0 0 1 27,27 V349 Z" fill="var(--navy)"/>
    <line x1="654" y1="258" x2="1086" y2="258" stroke="var(--crease)" stroke-width="1"/>
    <path d="M654,881 H1086 V1007 a27,27 0 0 1 -27,27 H681 a27,27 0 0 1 -27,-27 Z" fill="var(--navy)"/>
    <line x1="654" y1="973" x2="1086" y2="973" stroke="var(--crease)" stroke-width="1"/>

    <polygon points="1086,350 1105,350 1133,384 1133,853 1105,871 1086,881" fill="var(--orange)"/>
    <g stroke="var(--navy)" stroke-width="1.2">
      <line x1="1099" y1="432" x2="1120" y2="404"/>
      <line x1="1099" y1="462" x2="1120" y2="434"/>
      <line x1="1099" y1="492" x2="1120" y2="464"/>
      <line x1="1099" y1="522" x2="1120" y2="494"/>
      <line x1="1099" y1="552" x2="1120" y2="524"/>
      <line x1="1099" y1="582" x2="1120" y2="554"/>
      <line x1="1099" y1="612" x2="1120" y2="584"/>
      <line x1="1099" y1="642" x2="1120" y2="614"/>
      <line x1="1099" y1="672" x2="1120" y2="644"/>
      <line x1="1099" y1="702" x2="1120" y2="674"/>
      <line x1="1099" y1="732" x2="1120" y2="704"/>
      <line x1="1099" y1="762" x2="1120" y2="734"/>
      <line x1="1099" y1="792" x2="1120" y2="764"/>
      <line x1="1099" y1="822" x2="1120" y2="794"/>
    </g>
  </svg>

  <div class="spine-label spine-left product-name">Recipe Cards</div>
  <div class="spine-label spine-mid product-name">Recipe Cards</div>

  <!-- Back panel -->
  <div class="panel" style="left:134px; top:349px; width:432px; height:532px;" role="img" aria-label="Hand-drawn food sketches over soft yellow, green, orange and mint colour blobs"></div>
  <div class="card" style="left:164px; top:397px; width:363px; height:447px;"></div>
  <div class="frame" style="left:179px; top:416px; width:328px; height:411px;"></div>
  <div class="ornament" style="left:188px; top:425px;" role="img" aria-label="Corner flourish ornament"></div>
  <div class="ornament" style="left:416px; top:425px;" role="img" aria-label="Corner flourish ornament"></div>
  <div class="ornament" style="left:188px; top:737px;" role="img" aria-label="Corner flourish ornament"></div>
  <div class="ornament" style="left:416px; top:737px;" role="img" aria-label="Corner flourish ornament"></div>
  <p class="back-copy">Lorem ipsum dolor sit amet, consectetuer adipiscing elit, sed diam nonummy nibh euismod tincidunt ut laoreet dolore magna aliquam erat volutpat. Ut wisi enim ad minim veniam, quis nostrud exerci tation ullamcorper suscipit lobortis nisl ut aliquip ex ea commodo consequat. Duis autem vel eum iriure dolor in hendrerit in vulputate velit esse molestie consequat, vel</p>

  <!-- Front panel -->
  <div class="panel" style="left:654px; top:349px; width:432px; height:532px;" role="img" aria-label="Hand-drawn food sketches over soft yellow, green, orange and mint colour blobs"></div>
  <div class="card" style="left:694px; top:392px; width:362px; height:446px;"></div>
  <div class="frame" style="left:711px; top:408px; width:330px; height:412px;"></div>
  <div class="ornament" style="left:720px; top:418px;" role="img" aria-label="Corner flourish ornament"></div>
  <div class="ornament" style="left:950px; top:418px;" role="img" aria-label="Corner flourish ornament"></div>
  <div class="ornament" style="left:720px; top:727px;" role="img" aria-label="Corner flourish ornament"></div>
  <div class="ornament" style="left:950px; top:727px;" role="img" aria-label="Corner flourish ornament"></div>
  <div class="ornament center" style="left:838px; top:423px;" role="img" aria-label="Centre fleur ornament"></div>
  <div class="ornament center-wide" style="left:813px; top:770px;" role="img" aria-label="Centre scroll ornament"></div>

  <div class="title-block">
    <div class="title-rule"></div>
    <h1 class="title-text product-name">Recipe<br>Cards</h1>
  </div>
  <p class="tagline">EVERYDAY RECIPES FOR COOKING WITH HONEY</p>

</div>
</body>
</html>
```